Security doors and flyscreens

We need business cards for our company called K & R Traders. We quote, manufacture and install security doors and flyscreens.

Industry/Entity Type

Security

Contact Information for Business Card

K & R TRADERS
17 Larkfield Ave. Sampleton 0000
Ph: (03) 5550 1234
Fax: (03) 5550 1235
Colin: 0491 570 156
Email: gatemakerhub@mailbox-example.net

```html
<!DOCTYPE html>
<html lang="en">
<head>
<meta charset="utf-8">
<title>K &amp; R Traders – Business Card</title>
<link rel="stylesheet" href="https://fonts.googleapis.com/css2?family=Orbitron:wght@600&family=Exo+2:wght@400;500&display=swap">
<style>
  :root {
    --page-bg: #e9ecef;
    --card-bg: #ffffff;
    --brand-blue: #1ea4de;
    --brand-blue-dark: #1388c0;
    --social-navy: #3f4a9a;
    --ink: #222428;
    --white: #ffffff;
  }
  * { box-sizing: border-box; margin: 0; padding: 0; }
  html, body { width: 1200px; height: 828px; overflow: hidden; }
  body {
    background: var(--page-bg);
    font-family: "Exo 2", "Segoe UI", sans-serif;
    color: var(--ink);
    position: relative;
  }
  .card {
    position: absolute;
    left: 268px;
    width: 664px;
    height: 380px;
    background: var(--card-bg);
    box-shadow: 0 6px 18px rgba(0,0,0,0.14);
    overflow: hidden;
  }
  .card--front { top: 22px; }
  .card--back  { top: 426px; }

  .brand { position: absolute; display: flex; align-items: center; gap: 14px; }
  .brand__mark { width: 46px; height: 46px; background: var(--brand-blue); flex: none; }
  .brand__name {
    font-family: "Orbitron", "Arial Black", sans-serif;
    font-weight: 600;
    font-size: 20px;
    letter-spacing: 1px;
    color: var(--ink);
    white-space: nowrap;
  }
  .card--front .brand { left: 34px; top: 30px; }
  .card--back .brand { left: 50%; top: 50%; transform: translate(-50%, -50%); flex-direction: column; gap: 18px; }
  .card--back .brand__mark { width: 84px; height: 84px; }

  .band { position: absolute; left: 0; top: 150px; width: 664px; height: 48px; }
  .holder { position: absolute; left: 22px; top: 152px; color: var(--white); }
  .holder__name { font-size: 15px; font-weight: 500; letter-spacing: 1px; line-height: 17px; }
  .holder__title { font-size: 10px; line-height: 12px; }

  .socials { position: absolute; right: 0; top: 34px; list-style: none; }
  .socials li { display: flex; align-items: center; justify-content: flex-end; height: 36px; font-size: 14px; color: var(--ink); white-space: nowrap; }
  .socials .dot { width: 26px; height: 26px; border-radius: 50%; margin-left: 10px; flex: none; }
  .socials .dot--a { background: var(--social-navy); }
  .socials .dot--b, .socials .dot--c { background: var(--brand-blue); }
  .socials .lead { width: 28px; height: 2px; background: var(--brand-blue); flex: none; }
  .socials li:first-child .lead { background: var(--social-navy); }

  .contacts { position: absolute; left: 30px; top: 218px; list-style: none; }
  .contacts li { display: flex; align-items: flex-start; gap: 10px; font-size: 15px; line-height: 19px; margin-bottom: 10px; letter-spacing: 0.5px; white-space: nowrap; }
  .icon { width: 18px; height: 18px; flex: none; margin-top: 1px; }

  .online { position: absolute; left: 352px; top: 292px; list-style: none; }
  .online li { display: flex; align-items: center; gap: 10px; font-size: 14px; line-height: 18px; margin-bottom: 12px; white-space: nowrap; }
</style>
</head>
<body>

<section class="card card--front" aria-label="Business card front">
  <div class="brand">
    <span class="brand__mark"></span>
    <span class="brand__name">K &amp; R TRADERS</span>
  </div>

  <ul class="socials">
    <li>social.example/krtraders<span class="dot dot--a"></span><span class="lead"></span></li>
    <li>@krtraders<span class="dot dot--b"></span><span class="lead"></span></li>
    <li>krtraders.call<span class="dot dot--c"></span><span class="lead"></span></li>
  </ul>

  <svg class="band" viewBox="0 0 664 48" aria-hidden="true">
    <rect x="0" y="0" width="262" height="34" fill="var(--brand-blue)"/>
    <polygon points="272,0 284,0 300,34 288,34" fill="var(--brand-blue)"/>
    <polygon points="292,0 304,0 320,34 308,34" fill="var(--brand-blue)"/>
    <polygon points="312,0 324,0 340,34 328,34" fill="var(--brand-blue)"/>
    <polygon points="332,0 344,0 360,34 348,34" fill="var(--brand-blue)"/>
    <rect x="0" y="38" width="664" height="4" fill="var(--brand-blue-dark)"/>
  </svg>
  <div class="holder">
    <div class="holder__name">COLIN REEVES</div>
    <div class="holder__title">Managing Director</div>
  </div>

  <ul class="contacts">
    <li>
      <svg class="icon" viewBox="0 0 18 18" aria-hidden="true"><circle cx="9" cy="9" r="9" fill="var(--ink)"/><path d="M6 4.5c.6 0 1 .8 1.3 1.6.2.5-.4.9-.6 1.2.5 1.3 1.6 2.5 3 3 .3-.2.7-.8 1.2-.6.8.3 1.6.7 1.6 1.3 0 .9-1 1.5-1.8 1.5C7.6 12.5 5 10 4.5 6.3c0-.9.6-1.8 1.5-1.8z" fill="var(--white)"/></svg>
      Ph: (03) 5550 1234
    </li>
    <li>
      <svg class="icon" viewBox="0 0 18 18" aria-hidden="true"><circle cx="9" cy="9" r="9" fill="var(--ink)"/><rect x="6" y="4" width="6" height="3" fill="var(--white)"/><rect x="4.5" y="7.5" width="9" height="4" rx="1" fill="var(--white)"/><rect x="6" y="10" width="6" height="3.5" fill="var(--white)"/></svg>
      Fax: (03) 5550 1235
    </li>
    <li>
      <svg class="icon" viewBox="0 0 18 18" aria-hidden="true"><circle cx="9" cy="9" r="9" fill="var(--ink)"/><path d="M9 3.8a3.3 3.3 0 0 1 3.3 3.3C12.3 9.6 9 14 9 14S5.7 9.6 5.7 7.1A3.3 3.3 0 0 1 9 3.8z" fill="var(--white)"/><circle cx="9" cy="7.1" r="1.3" fill="var(--ink)"/></svg>
      <span>17 Larkfield Ave.<br>Sampleton 0000</span>
    </li>
    <li>
      <svg class="icon" viewBox="0 0 18 18" aria-hidden="true"><circle cx="9" cy="9" r="9" fill="var(--ink)"/><rect x="6" y="3.8" width="6" height="10.4" rx="1.2" fill="var(--white)"/><rect x="7" y="5" width="4" height="6.5" fill="var(--ink)"/></svg>
      Colin: 0491 570 156
    </li>
  </ul>

  <ul class="online">
    <li>
      <svg class="icon" viewBox="0 0 18 18" aria-hidden="true"><circle cx="9" cy="9" r="9" fill="var(--ink)"/><rect x="4.5" y="5.5" width="9" height="7" fill="var(--white)"/><path d="M4.5 5.5 9 9.5l4.5-4" stroke="var(--ink)" fill="none" stroke-width="1"/></svg>
      gatemakerhub@mailbox-example.net
    </li>
    <li>
      <svg class="icon" viewBox="0 0 18 18" aria-hidden="true"><circle cx="9" cy="9" r="9" fill="var(--ink)"/><circle cx="9" cy="9" r="5" fill="none" stroke="var(--white)" stroke-width="1.2"/><ellipse cx="9" cy="9" rx="2.2" ry="5" fill="none" stroke="var(--white)" stroke-width="1"/><line x1="4" y1="9" x2="14" y2="9" stroke="var(--white)" stroke-width="1"/></svg>
      www.krtraders-example.com
    </li>
  </ul>
</section>

<section class="card card--back" aria-label="Business card back">
  <div class="brand">
    <span class="brand__mark"></span>
    <span class="brand__name">K &amp; R TRADERS</span>
  </div>
</section>

</body>
</html>
```